Plakate für Charity Unternehmen
Zielgruppe
Orno ist ein weltweit agierendes Charity Unternehmen.
Aufgabenstellung
Wir benötigen ein 'Plakat' Design, mit dem Zweck dieses Design als Banner, Sticker oder als Schild an unseren Projekten anzubringen. Das Schild soll in zwei verschiedenen Layouts geliefert werden.
1. Eine Art Blanko Version in der das Logo und das Motto eingearbeitet sind. Dieser Teil nimmt rund 1/3 des Plakats ein. Der Rest hat einen Freiraum auf dem wir Namen der Spender oder kooperative Charity Logos einsetzen können. Diese Version wird für Zusammenarbeit verwendet.
2. Eine zweite Version nimmt das gesamte Plakat ein, hier findet sich das Logo und das Motto welche das ganze Plakat einnehmen.
In beiden Fällen sollte die Aufteilung sauber und gut leserlich sein. Das Plakat wird in Auflösungen von bis zu 1,5m mal 1m gedruckt, sollte dementsprechend also die richtige Auflösung haben. Außerdem sollten Photoshop Datei möglichst mitgeliefert werden damit wir wenn nötig Namen und Logos einsetzen können.
Das einzuarbeitende Motto lautet:
إنما المؤمنون أخوة
Das Plakat sollte im Querformat sein und die Hintergrundfarbe sollte schwarz oder weiß sein.
Anbei befindet sich eine Beispieldatei wie das Plakat an den Projekten angebracht wird.

```html
<!DOCTYPE html>
<html lang="de">
<head>
<meta charset="utf-8">
<title>Orno – Plakat Entwürfe</title>
<link rel="stylesheet" href="https://fonts.googleapis.com/css2?family=Tajawal:wght@700;800&display=swap">
<style>
  :root {
    --page-bg: #fafafa;
    --poster-bg: #222222;
    --motto: #ffffff;
    --brand: #f3f3f3;
    --red-light: #c84a2a;
    --red-dark: #b8302a;
    --blue-light: #3d8fd6;
    --blue-dark: #2f72bb;
  }
  html, body {
    margin: 0;
    padding: 0;
    width: 1000px;
    height: 1200px;
    overflow: hidden;
    background: var(--page-bg);
  }
  .sheet {
    position: relative;
    width: 1000px;
    height: 1200px;
  }
  .poster {
    position: absolute;
    left: 108px;
    width: 784px;
    height: 522px;
    background: var(--poster-bg);
    overflow: hidden;
  }
  .poster--full { top: 65px; }
  .poster--blank { top: 613px; }
  .poster svg {
    display: block;
    width: 100%;
    height: 100%;
  }
  .motto {
    font-family: "Tajawal", sans-serif;
    font-weight: 800;
    font-size: 158px;
    fill: var(--motto);
  }
  .brand-name {
    font-family: "Tajawal", sans-serif;
    font-weight: 700;
    font-size: 84px;
    letter-spacing: 4px;
    fill: var(--brand);
  }
</style>
</head>
<body>
<main class="sheet">

  <section class="poster poster--full" aria-label="Plakat Version 2, volle Fläche">
    <svg viewBox="0 0 1371 914" preserveAspectRatio="none">
      <defs>
        <linearGradient id="redBand" x1="0" y1="0" x2="1" y2="0">
          <stop offset="0" stop-color="var(--red-light)"/>
          <stop offset="1" stop-color="var(--red-dark)"/>
        </linearGradient>
        <linearGradient id="blueBand" x1="0" y1="0" x2="1" y2="0">
          <stop offset="0" stop-color="var(--blue-light)"/>
          <stop offset="1" stop-color="var(--blue-dark)"/>
        </linearGradient>
      </defs>
      <polygon class="band band--red" points="51,412 1371,64 1371,124" fill="url(#redBand)"/>
      <polygon class="band band--blue" points="0,697 1328,406 0,757" fill="url(#blueBand)"/>
      <text class="motto" x="685" y="455" text-anchor="middle" direction="rtl" transform="rotate(-14.3 685 455)">إنما المؤمنون أخوة</text>
      <text class="brand-name" x="1144" y="832" text-anchor="middle">Velora</text>
    </svg>
  </section>

  <section class="poster poster--blank" aria-label="Plakat Version 1, mit Freiraum für Spender">
    <svg viewBox="0 0 1371 914" preserveAspectRatio="none">
      <defs>
        <linearGradient id="redBand2" x1="0" y1="0" x2="1" y2="0">
          <stop offset="0" stop-color="var(--red-light)"/>
          <stop offset="1" stop-color="var(--red-dark)"/>
        </linearGradient>
        <linearGradient id="blueBand2" x1="0" y1="0" x2="1" y2="0">
          <stop offset="0" stop-color="var(--blue-light)"/>
          <stop offset="1" stop-color="var(--blue-dark)"/>
        </linearGradient>
      </defs>
      <polygon class="band band--red" points="51,412 1371,64 1371,122" fill="url(#redBand2)"/>
      <polygon class="band band--blue" points="0,690 1371,393 0,757" fill="url(#blueBand2)"/>
      <text class="motto" x="685" y="450" text-anchor="middle" direction="rtl" transform="rotate(-14.3 685 450)">إنما المؤمنون أخوة</text>
      <text class="brand-name" x="211" y="295" text-anchor="middle">Velora</text>
    </svg>
  </section>

</main>
</body>
</html>
```